Dale Harwick Terrain Services LLC

Need a business card design for a new company based in Cedar Hollow, TX. We specialize in under-brush clearing, forestry mulching, cutover mulching, right of way clearing, land line & fence row clearing, bush hogging, land clearing, wildlife food plots. We use compact track loaders and tractors. I will attach a picture of a compact track loader I would like to have on the card design if possible.

Target Market(s)

Businesses / Land Owners

Contact Information for Business Card

Dale Harwick
Owner / Operator

Cedar Hollow, TX

Call/Text: 601-555-3871
dhterrainwork@mailvista.test
FB: @daleharwickterrainservicesllc

Font styles to use
Serif
Sans Serif

Requirements
Must have
• Contact info, city & state. Description of services.
Nice to have
• Not overwhelming back ground but eye and interest catching with clear objection of the business

```html
<!DOCTYPE html>
<html lang="en">
<head>
<meta charset="utf-8">
<title>Dale Harwick Terrain Services LLC — Business Card</title>
<link href="https://fonts.googleapis.com/css2?family=Montserrat:wght@400;500;700;800&display=swap" rel="stylesheet">
<style>
  :root {
    --amber-deep: #f0a92a;
    --amber-bright: #fdc90d;
    --ink: #111111;
    --ink-soft: #3a2f12;
    --paper-white: #ffffff;
    --frame-brown: #6e5a2a;
    --canvas-bg: #e9e7e2;
    --photo-green: #3d5a2c;
    --photo-yellow: #d9a51e;
  }
  * { margin: 0; padding: 0; box-sizing: border-box; }
  html, body { width: 1200px; height: 1067px; overflow: hidden; }
  body {
    background: var(--canvas-bg);
    font-family: "Montserrat", sans-serif;
    color: var(--ink);
    position: relative;
  }
  .card {
    position: absolute;
    left: 180px;
    width: 840px;
    height: 480px;
    background: linear-gradient(90deg, var(--amber-deep), var(--amber-bright));
    box-shadow: 0 10px 24px rgba(0,0,0,.25);
    overflow: hidden;
  }
  .card--back { top: 36px; }
  .card--front { top: 551px; }

  /* Back side */
  .services {
    position: absolute;
    left: 56px;
    top: 118px;
    width: 410px;
  }
  .services__title {
    font-weight: 700;
    font-size: 26px;
    margin-bottom: 12px;
  }
  .services__list {
    font-size: 17px;
    line-height: 1.42;
    font-weight: 400;
  }
  .contact {
    position: absolute;
    left: 56px;
    top: 360px;
    font-size: 17px;
    line-height: 1.7;
  }
  .contact__label { font-weight: 700; margin-right: 6px; }
  .machine-photo {
    position: absolute;
    right: 56px;
    top: 60px;
    width: 300px;
    height: 300px;
    border-radius: 50%;
    border: 6px solid var(--frame-brown);
    background: linear-gradient(180deg, var(--photo-green) 0%, #2a3d22 45%, var(--photo-yellow) 70%, #5e8d3a 100%);
  }

  /* Front side */
  .owner {
    position: absolute;
    right: 64px;
    top: 58px;
    text-align: right;
  }
  .owner__name {
    font-weight: 800;
    font-size: 44px;
    letter-spacing: .5px;
    line-height: 1;
  }
  .owner__role {
    font-weight: 500;
    font-size: 17px;
    margin-top: 6px;
  }
  .band {
    position: absolute;
    left: 0;
    right: 0;
    top: 250px;
    height: 120px;
    background: var(--ink);
    color: var(--paper-white);
    display: flex;
    align-items: center;
    justify-content: space-between;
    padding: 0 56px;
  }
  .brand {
    display: flex;
    align-items: center;
    gap: 16px;
  }
  .brand__mark {
    width: 44px;
    height: 44px;
    border-radius: 50%;
    background: var(--amber-bright);
    flex: none;
  }
  .brand__name {
    font-weight: 700;
    font-size: 24px;
    line-height: 1.15;
    color: var(--paper-white);
  }
  .phone {
    font-weight: 800;
    font-size: 50px;
    letter-spacing: 1px;
  }
  .location {
    position: absolute;
    left: 0;
    right: 0;
    top: 400px;
    text-align: center;
    font-weight: 500;
    font-size: 26px;
    letter-spacing: 18px;
    padding-left: 18px;
    color: var(--ink-soft);
  }
</style>
</head>
<body>

  <section class="card card--back" aria-label="Card back">
    <div class="services">
      <h2 class="services__title">We are specialize in...</h2>
      <p class="services__list">Under-Brush Clearing, Forestry Mulching, Cutover Mulching, Right of Way Clearing, Land line &amp; Fence Row Clearing, Bush Hogging, Land Clearing, Wildlife Food Plots</p>
    </div>
    <div class="contact">
      <p><span class="contact__label">E:</span>dhterrainwork@mailvista.test</p>
      <p><span class="contact__label">FB:</span>@daleharwickterrainservicesllc</p>
    </div>
    <div class="machine-photo" role="img" aria-label="Photo of a yellow compact track loader with a forestry mulcher attachment on grass in front of trees"></div>
  </section>

  <section class="card card--front" aria-label="Card front">
    <div class="owner">
      <p class="owner__name">DALE HARWICK</p>
      <p class="owner__role">OWNER</p>
    </div>
    <div class="band">
      <div class="brand">
        <span class="brand__mark" aria-hidden="true"></span>
        <p class="brand__name">DALE HARWICK<br>TERRAIN SERVICES LLC</p>
      </div>
      <p class="phone">601-555-3871</p>
    </div>
    <p class="location">CEDAR HOLLOW, TX</p>
  </section>

</body>
</html>
```